Stationery Required - Own Logo provided

Hi,

We are a retail company called 'Copperfinch Trading Limited' based in the UK and would like some corporate stationery designed.

We have provided our Logo which we would like to use (Its attached to this brief)...

The designs must be orginal, professional, stylish and interesting!

Target Market(s)

We will use this stationery to communicate with our wholesale suppliers and employees, so it must have a 'professional' feel about it.

Industry/Entity Type

It Company

Requirements
Must have
• Must be professional, corporate, stylish and not to 'fussy'. we require ... Business card design, a4 letter, compliment slip. All designs must be supplied in a format where the text (address/telephone numbers etc..) can be edited, as we have alot of staff and operate out of several different premises.
Nice to have
• I would like a windows backround picture file supplied as well so we can integrate that onto our computer systems.

```html
<!DOCTYPE html>
<html lang="en">
<head>
<meta charset="utf-8">
<title>Copperfinch Trading Limited – With Compliments</title>
<link rel="stylesheet" href="https://fonts.googleapis.com/css2?family=Montserrat:wght@700&family=Questrial&display=swap">
<style>
  :root {
    --lime: #84ff00;
    --forest: #275a00;
    --forest-text: #2e6a00;
    --paper: #ffffff;
    --ink-light: #ffffff;
  }
  * { margin: 0; padding: 0; box-sizing: border-box; }
  html, body { width: 1200px; height: 565px; overflow: hidden; background: var(--paper); }
  .slip {
    position: relative;
    width: 1200px;
    height: 565px;
    overflow: hidden;
    background: var(--paper);
    font-family: "Montserrat", Arial, sans-serif;
  }
  .top-band {
    position: absolute; left: 0; top: 0;
    width: 100%; height: 40px;
    background: var(--lime);
  }
  .brand {
    position: absolute;
    right: 72px; top: 104px;
    display: flex; align-items: center; gap: 14px;
  }
  .brand-square {
    width: 34px; height: 34px;
    background: var(--lime);
  }
  .brand-name {
    font-family: "Questrial", Arial, sans-serif;
    font-size: 31px;
    color: var(--forest-text);
    letter-spacing: 0.5px;
    white-space: nowrap;
  }
  .greeting {
    position: absolute;
    left: 72px; top: 374px;
    font-size: 29px;
    font-weight: 700;
    color: var(--lime);
  }
  .footer-wave {
    position: absolute; left: 0; top: 0;
    width: 1200px; height: 565px;
  }
  .wave-edge { fill: var(--lime); }
  .wave-body { fill: var(--forest); }
  .footer-name {
    position: absolute;
    left: 66px; top: 480px;
    font-size: 18px;
    font-weight: 700;
    color: var(--ink-light);
  }
  .contact {
    position: absolute;
    top: 461px;
    height: 67px;
    border-left: 2px solid var(--ink-light);
    padding-left: 9px;
    color: var(--ink-light);
    font-size: 14.2px;
    font-weight: 700;
    line-height: 17px;
  }
  .contact-address { left: 193px; }
  .contact-lines { left: 383px; }
  .contact-lines dl {
    display: grid;
    grid-template-columns: 59px auto;
  }
  .contact-lines dd { margin: 0; }
</style>
</head>
<body>
  <main class="slip">
    <div class="top-band"></div>

    <div class="brand">
      <span class="brand-square"></span>
      <span class="brand-name">Copperfinch Trading Limited</span>
    </div>

    <p class="greeting">with compliments</p>

    <svg class="footer-wave" viewBox="0 0 1200 565" aria-hidden="true">
      <path class="wave-edge" d="M0 414 L520 414 C860 416 1080 440 1200 512 L1200 565 L0 565 Z"/>
      <path class="wave-body" d="M0 422 L520 422 C850 424 1060 450 1200 524 L1200 565 L0 565 Z"/>
    </svg>

    <p class="footer-name">Copperfinch</p>

    <address class="contact contact-address">
      17 Mill Brae Road<br>
      Ballykeel<br>
      County Down<br>
      BT30 4QX
    </address>

    <div class="contact contact-lines">
      <dl>
        <dt>Tel:</dt><dd>07700 900 418</dd>
        <dt>Fax:</dt><dd>????? ??? ???</dd>
        <dt>Email:</dt><dd>hello@copperfinchtrading.co.uk</dd>
        <dt>Web:</dt><dd>www.???????????????</dd>
      </dl>
    </div>
  </main>
</body>
</html>
```